Wedding Invitations

We are a printing company "inkmorrow" and require multiple wedding invitation designs for our customers in store and online. We would like the designs to be editable in Photoshop if possible, if not then a layout with suggested fonts would be the next best option. We are open to suggestions on design but would like to stick to the general wedding themes some with a modern and some with a classical feel

Industry/Entity Type

Printing

```html
<!DOCTYPE html>
<html lang="en">
<head>
<meta charset="utf-8">
<title>Wedding Invitation – Rosalind &amp; Thomas</title>
<link href="https://fonts.googleapis.com/css2?family=Great+Vibes&family=Poiret+One&display=swap" rel="stylesheet">
<style>
  :root {
    --blush: #efc4bc;
    --rule: #efc4bc;
    --ink: #3a3a3a;
    --paper: #ffffff;
  }
  html, body {
    margin: 0;
    padding: 0;
    overflow: hidden;
    background: var(--paper);
  }
  .invitation {
    position: relative;
    width: 805px;
    height: 1200px;
    overflow: hidden;
    background: var(--paper);
    font-family: "Poiret One", sans-serif;
    color: var(--ink);
    text-transform: uppercase;
  }
  .monogram {
    position: absolute;
    inset: 0;
    font-family: "Great Vibes", cursive;
    color: var(--blush);
    text-transform: none;
    line-height: 1;
    pointer-events: none;
  }
  .monogram span {
    position: absolute;
    white-space: nowrap;
    transform-origin: left bottom;
  }
  .monogram-first {
    left: 30px;
    top: 60px;
    font-size: 250px;
    transform: rotate(-19deg);
  }
  .monogram-amp {
    left: -10px;
    top: 210px;
    font-size: 250px;
    transform: rotate(-19deg);
  }
  .monogram-second {
    left: 330px;
    top: 160px;
    font-size: 250px;
    transform: rotate(-19deg);
  }
  .line {
    position: absolute;
    left: 0;
    right: 0;
    text-align: center;
    white-space: nowrap;
    margin: 0;
    font-weight: 400;
  }
  .couple-name { font-size: 50px; letter-spacing: 1px; }
  .bride { top: 562px; }
  .groom { top: 650px; }
  .joiner {
    top: 630px;
    font-size: 16px;
    letter-spacing: 1px;
  }
  .joiner-rule {
    position: absolute;
    top: 641px;
    height: 2px;
    background: var(--rule);
  }
  .joiner-rule.left { left: 185px; width: 190px; }
  .joiner-rule.right { left: 430px; width: 194px; }
  .invite-line { top: 741px; font-size: 20px; letter-spacing: 1.5px; }
  .date { top: 806px; font-size: 30px; }
  .time { top: 846px; font-size: 19px; letter-spacing: 1px; }
  .venue { top: 900px; font-size: 30px; }
  .venue-address { top: 942px; font-size: 15px; letter-spacing: 1px; }
  .divider {
    position: absolute;
    left: 120px;
    width: 568px;
    background: var(--rule);
  }
  .divider.upper { top: 1030px; height: 4px; }
  .divider.lower { top: 1040px; height: 2px; left: 130px; width: 548px; }
  .reception { top: 1073px; font-size: 28px; }
  .reception-address { top: 1122px; font-size: 19px; letter-spacing: 0.5px; }
  .reception-address .numeral { font-size: 27px; }
</style>
</head>
<body>
  <main class="invitation">
    <div class="monogram" aria-hidden="true">
      <span class="monogram-first">Rosalind</span>
      <span class="monogram-amp">&amp;</span>
      <span class="monogram-second">Thomas</span>
    </div>

    <h1 class="line couple-name bride">Rosalind Hale</h1>
    <span class="joiner-rule left"></span>
    <p class="line joiner">and</p>
    <span class="joiner-rule right"></span>
    <h1 class="line couple-name groom">Thomas Ashby</h1>

    <p class="line invite-line">Tie the knot and warmly invite you to join them</p>

    <p class="line date">Saturday April 12 2014</p>
    <p class="line time">At half past ten in the morning</p>

    <p class="line venue">The Willowmere Gardens, Harbourside The Terrace,</p>
    <p class="line venue-address">Cnr Linden Ave and Fairlie St, Eastbrook</p>

    <span class="divider upper"></span>
    <span class="divider lower"></span>

    <p class="line reception">Dinner &amp; Dancing to follow 5pm</p>
    <p class="line reception-address">The Ashcombe, Harbourside, <span class="numeral">1</span> Quayside Ave, Riverbank</p>
  </main>
</body>
</html>
```